Corporate Branding - Web and Print

A UK based company will like to use an existing logo to create branding materials for all marketing related documents, including business card, prints, letterhead, Website, Twitter, Facebook, Instagram logo etc. This company serves high-end clientele in the fashion, health and wellness and as such high quality and class is of utmost importance.
Where the logo can be modernised without losing its character then experiment. The main thing is to have a corporate branding which can be used later for brochures, Business Plan infographics.
The prominent colour within the organisation is burnt orange with no secondary colour. However if you believe a secondary colour is needed then use it, otherwise keep it simple and classy. Any chosen colours have to match perfectly.
Target Market(s)
High net worth individuals
Industry/Entity Type
Health And Wellness
Contact Information for Business Card
classy

```html
<!DOCTYPE html>
<html lang="en">
<head>
<meta charset="utf-8">
<title>Nuvariq Business Card</title>
<link rel="stylesheet" href="https://fonts.googleapis.com/css2?family=Montserrat:wght@400;700&family=Open+Sans:wght@400;600&display=swap">
<style>
  :root {
    --gold: #f0ae1e;
    --ink: #1f1f1f;
    --card-dark: #1c1c1c;
    --paper: #ffffff;
    --text: #3a3a3a;
    --backdrop: #e6e3de;
  }
  * { box-sizing: border-box; margin: 0; padding: 0; }
  html, body { width: 1200px; height: 780px; overflow: hidden; }
  body {
    background: var(--backdrop);
    display: flex;
    align-items: center;
    justify-content: center;
    gap: 40px;
    font-family: "Open Sans", sans-serif;
  }
  .card {
    position: relative;
    width: 540px;
    height: 310px;
    border-radius: 3px;
    overflow: hidden;
    box-shadow: 0 10px 28px rgba(0,0,0,0.18);
  }
  .card-front { background: var(--paper); }
  .card-back {
    background: var(--card-dark);
    display: flex;
    align-items: center;
    justify-content: center;
  }
  .wave { position: absolute; inset: 0; width: 100%; height: 100%; }
  .brand {
    display: flex;
    align-items: center;
    gap: 12px;
    font-family: "Montserrat", sans-serif;
    font-weight: 700;
    color: var(--gold);
    letter-spacing: 1px;
    white-space: nowrap;
  }
  .brand-mark { border-radius: 50%; background: var(--gold); flex: none; }
  .card-front .brand { position: absolute; top: 44px; right: 40px; font-size: 38px; }
  .card-front .brand-mark { width: 36px; height: 36px; }
  .card-back .brand { font-size: 48px; }
  .card-back .brand-mark { width: 46px; height: 46px; }
  .holder { position: absolute; left: 36px; top: 122px; }
  .holder-name {
    font-family: "Montserrat", sans-serif;
    font-weight: 700;
    font-size: 18px;
    color: var(--ink);
    letter-spacing: 0.3px;
  }
  .holder-role { font-size: 12px; color: var(--gold); margin-top: 1px; }
  .address {
    position: absolute;
    left: 36px;
    top: 172px;
    font-size: 11.5px;
    line-height: 16px;
    color: var(--text);
  }
  .contacts {
    position: absolute;
    left: 36px;
    top: 214px;
    list-style: none;
    font-size: 11.5px;
    color: var(--text);
  }
  .contacts li { display: flex; align-items: center; gap: 7px; height: 19px; }
  .contact-icon { width: 15px; height: 15px; flex: none; }
</style>
</head>
<body>
  <section class="card card-front">
    <svg class="wave" viewBox="0 0 540 310" preserveAspectRatio="none" aria-hidden="true">
      <path d="M0 310 C 180 300, 330 238, 540 128 L540 310 Z" fill="var(--gold)"/>
      <path d="M0 310 C 195 306, 350 252, 540 146 L540 310 Z" fill="var(--ink)"/>
    </svg>
    <div class="brand"><span class="brand-mark"></span>NUVARIQ</div>
    <div class="holder">
      <p class="holder-name">LENA MARSH</p>
      <p class="holder-role">Managing Partner</p>
    </div>
    <p class="address">PO BOX 48 Harrow Lane<br>7th street Leeds UK</p>
    <ul class="contacts">
      <li>
        <svg class="contact-icon" viewBox="0 0 16 16" aria-hidden="true"><circle cx="8" cy="8" r="8" fill="var(--gold)"/><path d="M5.2 4.2l1.6 0 .7 2-1 .8a5 5 0 0 0 2.5 2.5l.8-1 2 .7v1.6c0 .5-.4.8-.9.8A6.6 6.6 0 0 1 4.4 5.1c0-.5.3-.9.8-.9z" fill="#fff"/></svg>
        (02) 4817 3920
      </li>
      <li>
        <svg class="contact-icon" viewBox="0 0 16 16" aria-hidden="true"><circle cx="8" cy="8" r="8" fill="var(--gold)"/><rect x="4" y="5.2" width="8" height="5.6" rx="0.6" fill="#fff"/><path d="M4.3 5.6 8 8.5l3.7-2.9" fill="none" stroke="var(--gold)" stroke-width="0.9"/></svg>
        hello@nuvariqwell.com
      </li>
      <li>
        <svg class="contact-icon" viewBox="0 0 16 16" aria-hidden="true"><circle cx="8" cy="8" r="8" fill="var(--gold)"/><g fill="none" stroke="#fff" stroke-width="0.9"><circle cx="8" cy="8" r="4.2"/><ellipse cx="8" cy="8" rx="1.8" ry="4.2"/><path d="M3.8 8h8.4"/></g></svg>
        www.nuvariqwell.com
      </li>
    </ul>
  </section>

  <section class="card card-back">
    <div class="brand"><span class="brand-mark"></span>NUVARIQ</div>
  </section>
</body>
</html>
```